Long Established Local Fencing (not swords) Business needs fresh Business Cards

We need fresh double sided business cards for our Fencing Construction business, we are looking for something with our new logo design added, and maybe a photo background ?
We recently had cards made from Cardlyne and we were horrified with what we got back, the quality was terrible, so am looking for high quality format for good printing company to make.
We install Steelmora, Timber paling, Aluminium Slat Screening, Picket (timber and aluminium) and most other fencing installations.
Our website is brankelrails.com.au should you like to learn a bit more.
We do have logo in other formats if required.
We have been in business for over 35 years and we have used this as a "motto" it is on our signage

Industry/Entity Type

Construction

Contact Information for Business Card

Open to ideas, we need 3 x different cards, one generic with no name and 2 x others each with 1 of our bosses name on each, I will put into upload files.

Colors
ec1f27
000000
606060
f5f5f5

Requirements
Must have
• Company Name and Logo
• Address
• Contact details, phone, website, email etc
• Small space to write notes when leaving card at residence
Nice to have
• Our motto "Servicing the Peninsula for over 35 years"

```html
<!DOCTYPE html>
<html lang="en">
<head>
<meta charset="utf-8">
<title>Brankel Rails – Business Cards</title>
<link rel="stylesheet" href="https://fonts.googleapis.com/css2?family=Montserrat:wght@600;800&family=Questrial&display=swap">
<style>
  :root {
    --red: #ec1f27;
    --black: #000000;
    --grey: #606060;
    --paper: #f5f5f5;
    --white: #ffffff;
    --stage: #d9d9d9;
    --navy-dark: #1c2740;
    --navy: #34466e;
  }
  * { box-sizing: border-box; margin: 0; padding: 0; }
  html, body { width: 1200px; height: 1200px; overflow: hidden; }
  body {
    background: var(--stage);
    font-family: "Montserrat", sans-serif;
    position: relative;
  }
  .card {
    position: absolute;
    left: 180px;
    width: 840px;
    height: 510px;
    overflow: hidden;
    box-shadow: 0 6px 18px rgba(0,0,0,0.18);
  }
  .card--front { top: 60px; background: var(--paper); }
  .card--back { top: 630px; background: var(--black); }

  /* front */
  .front-photo {
    position: absolute; inset: 0;
    width: 380px;
    clip-path: polygon(0 0, 100% 0, 82% 100%, 0 100%);
    background: linear-gradient(160deg, #5d6d8c 0%, var(--navy) 35%, var(--navy-dark) 100%);
  }
  .front-band {
    position: absolute; left: 0; right: 0; top: 150px; height: 42px;
    background: var(--red);
  }
  .front-name {
    position: absolute; right: 30px; top: 150px; height: 42px;
    line-height: 42px; color: var(--white);
    font-weight: 800; font-size: 28px;
  }
  .brand {
    position: absolute; display: flex; align-items: center; gap: 16px;
  }
  .brand__dot { border-radius: 50%; background: var(--red); flex: none; }
  .brand__name { font-weight: 800; letter-spacing: 1px; text-transform: uppercase; }
  .card--front .brand { right: 30px; top: 52px; }
  .card--front .brand__dot { width: 54px; height: 54px; }
  .card--front .brand__name { font-size: 40px; color: var(--black); }

  .front-licence {
    position: absolute; left: 430px; top: 206px;
    font-family: "Questrial", sans-serif; font-size: 17px; color: var(--grey);
  }
  .front-address {
    position: absolute; left: 400px; top: 236px;
    font-family: "Questrial", sans-serif; font-size: 22px; color: var(--black);
  }
  .front-contacts {
    position: absolute; left: 328px; right: 0; top: 288px; height: 132px;
    background: var(--black);
    clip-path: polygon(5% 0, 100% 0, 100% 100%, 0 100%);
    color: var(--white);
    font-family: "Questrial", sans-serif; font-size: 23px;
    padding: 24px 30px 0 60px;
  }
  .contact-row { display: flex; align-items: center; gap: 8px; height: 42px; }
  .contact-row + .contact-row { margin-top: 4px; }
  .contact-row .gap { width: 30px; }
  .icon { width: 20px; height: 20px; flex: none; }

  /* back */
  .back-content {
    position: absolute; inset: 0;
    display: flex; flex-direction: column; align-items: center; justify-content: center;
    gap: 34px;
  }
  .card--back .brand { position: static; }
  .card--back .brand__dot { width: 70px; height: 70px; }
  .card--back .brand__name { font-size: 56px; color: var(--white); }
  .back-web {
    font-family: "Montserrat", sans-serif; font-weight: 600;
    font-size: 26px; letter-spacing: 3px; color: var(--red);
  }
</style>
</head>
<body>

<section class="card card--front">
  <div class="front-photo" role="img" aria-label="Photo of a dark blue steel panel fence in front of a weatherboard house"></div>
  <div class="front-band"></div>
  <div class="front-name">Dorian Kellett</div>

  <div class="brand">
    <span class="brand__dot"></span>
    <span class="brand__name">Brankel Rails</span>
  </div>

  <p class="front-licence">License No. 41726d</p>
  <p class="front-address">PO Box 218 Marlow Bay NSW 2291</p>

  <div class="front-contacts">
    <div class="contact-row">
      <svg class="icon" viewBox="0 0 24 24"><path fill="#ec1f27" d="M6.6 10.8a15.1 15.1 0 0 0 6.6 6.6l2.2-2.2c.3-.3.7-.4 1-.2 1.1.4 2.3.6 3.6.6.6 0 1 .4 1 1V20c0 .6-.4 1-1 1A17 17 0 0 1 3 4c0-.6.4-1 1-1h3.5c.6 0 1 .4 1 1 0 1.3.2 2.5.6 3.6.1.3 0 .7-.2 1z"/></svg>
      <span>: (02) 5550 1827</span>
      <span class="gap"></span>
      <svg class="icon" viewBox="0 0 24 24"><rect x="6" y="2" width="12" height="20" rx="2" fill="none" stroke="#ec1f27" stroke-width="2.4"/><circle cx="12" cy="18" r="1.3" fill="#ec1f27"/></svg>
      <span>: 0400 555 382</span>
    </div>
    <div class="contact-row">
      <svg class="icon" viewBox="0 0 24 24"><rect x="2" y="5" width="20" height="14" rx="1.5" fill="#ec1f27"/><path d="M3 6l9 7 9-7" fill="none" stroke="#000" stroke-width="1.6"/></svg>
      <span>: office@brankelrails.com.au</span>
    </div>
  </div>
</section>

<section class="card card--back">
  <div class="back-content">
    <div class="brand">
      <span class="brand__dot"></span>
      <span class="brand__name">Brankel Rails</span>
    </div>
    <p class="back-web">www.brankelrails.com.au</p>
  </div>
</section>

</body>
</html>
```